business stationery

have a gorgeous logo that needs to be incorporated on stationery. Was hoping to do something on letterhead that was a paper that looked like "bark" from a tree or something that resembled the "woods." Soft paper with some very basic natural elements. Same thing for business cards. Think American lakeside cabin. Organic. Natural. Calm and welcoming but clear to read and understand. Wanted to use alot of black.

Target Market(s)

buyers of Tobias Wrenfield home. Client that would have more than one home and in need of rare pieces and items to furnish an upmarket lakeside holiday cabin in the woods. Someone who treasures beautiful hand made items, organic foods and a real crackling fire but with money to burn in it!

Industry/Entity Type

Business

Requirements
Must have
• My logo
My business name
www.fernandcopper.example
Natural almost raw effect paper
My ABN: 62 307 514 928 (to be placed in small writing at the bottom of card/letterhead)
Nice to have
• The website will consist of a cabin door that you "open" with a creak sound effect and then you go "inside" to look at the various rooms to start shopping. Want to bring that element of texture and warmth into the stationary also.
Should not have
• Anything modern or hard to read items

```html
<!DOCTYPE html>
<html lang="en">
<head>
<meta charset="utf-8">
<title>Fern &amp; Copper — Stationery</title>
<link rel="stylesheet" href="https://fonts.googleapis.com/css2?family=Dosis:wght@400;600;700&family=Oswald:wght@500&family=Oranienbaum&display=swap">
<style>
  :root {
    --backdrop: #ffffff;
    --paper-light: #e6d5b6;
    --paper: #d9c39f;
    --paper-edge: #c9ae86;
    --maroon: #6a0f13;
    --ink: #141110;
    --white: #ffffff;
  }
  * { margin: 0; padding: 0; box-sizing: border-box; }
  html, body { width: 962px; height: 1200px; overflow: hidden; background: var(--backdrop); }
  .canvas { position: relative; width: 962px; height: 1200px; }

  .paper {
    background: radial-gradient(ellipse at 50% 45%, var(--paper-light) 0%, var(--paper) 60%, var(--paper-edge) 100%);
    overflow: hidden;
  }

  /* Letterhead */
  .letterhead {
    position: absolute; left: 143px; top: 138px; width: 663px; height: 936px;
    box-shadow: 3px 4px 8px rgba(0,0,0,.28);
  }
  .brand {
    position: absolute; display: flex; align-items: center; gap: 8px;
    font-family: "Oswald", sans-serif; font-weight: 500; color: var(--ink);
    letter-spacing: .02em; line-height: 1;
  }
  .letterhead .brand { left: 21px; top: 86px; font-size: 40px; }
  .brand-dot { width: 14px; height: 14px; border-radius: 50%; background: var(--ink); flex: none; }
  .letterhead .brand-byline {
    position: absolute; left: 210px; top: 138px;
    font-family: "Oranienbaum", serif; font-size: 6px; color: var(--maroon); letter-spacing: .05em;
  }
  .leaf-area {
    position: absolute; right: 0; top: 0; width: 265px; height: 221px;
    background: radial-gradient(ellipse at 70% 35%, var(--maroon) 0%, var(--maroon) 45%, rgba(106,15,19,0) 72%);
  }
  .footer-wave { position: absolute; left: 0; bottom: 0; width: 663px; height: 250px; display: block; }
  .footer-info {
    position: absolute; left: 21px; bottom: 35px; display: flex; gap: 25px; align-items: baseline;
    font-family: "Dosis", sans-serif; color: var(--white);
  }
  .footer-info .site { font-size: 13.5px; font-weight: 700; }
  .footer-info .abn { font-size: 10.5px; font-weight: 400; letter-spacing: .02em; }

  /* Business card */
  .card {
    position: absolute; left: 619px; top: 632px; width: 282px; height: 160px;
    border-radius: 8px; border: 1px solid #8a7a66;
    box-shadow: 2px 3px 6px rgba(0,0,0,.35);
  }
  .card-wave { position: absolute; inset: 0; width: 282px; height: 160px; display: block; }
  .card-leaf {
    position: absolute; left: 75px; top: 28px; width: 120px; height: 115px;
    background: radial-gradient(ellipse at center, rgba(245,236,220,.75) 0%, rgba(245,236,220,.4) 50%, rgba(245,236,220,0) 72%);
  }
  .card .brand { left: 20px; top: 36px; font-size: 17px; gap: 4px; }
  .card .brand-dot { width: 6px; height: 6px; }
  .card-name {
    position: absolute; left: 57px; top: 113px;
    font-family: "Oranienbaum", serif; font-size: 10.5px; color: var(--maroon);
  }
  .card-contact {
    position: absolute; right: 21px; top: 113px; text-align: right;
    font-family: "Oranienbaum", serif; color: var(--ink); line-height: 1.15;
  }
  .card-contact .site { font-size: 6.5px; display: block; }
  .card-contact .abn { font-size: 4.5px; display: block; }
</style>
</head>
<body>
<main class="canvas">

  <section class="letterhead paper" aria-label="Letterhead">
    <div class="leaf-area" role="img" aria-label="Large maroon maple leaf decoration"></div>
    <div class="brand"><span class="brand-dot"></span>FERN &amp; COPPER</div>
    <div class="brand-byline">BY MAREN HOLLIS</div>

    <svg class="footer-wave" viewBox="0 0 663 250" preserveAspectRatio="none" aria-hidden="true">
      <path d="M0,6 C40,150 260,215 663,250 L0,250 Z" fill="var(--ink)"/>
      <path d="M0,38 C60,165 290,222 663,250 L0,250 Z" fill="var(--maroon)"/>
    </svg>
    <div class="footer-info">
      <span class="site">www.fernandcopper.example</span>
      <span class="abn">ABN: 62 307 514 928</span>
    </div>
  </section>

  <section class="card paper" aria-label="Business card">
    <svg class="card-wave" viewBox="0 0 282 160" preserveAspectRatio="none" aria-hidden="true">
      <path d="M225,0 C255,20 275,55 282,110 L282,0 Z" fill="var(--maroon)"/>
      <path d="M245,0 C265,20 277,50 282,85 L282,0 Z" fill="var(--ink)"/>
      <path d="M258,0 C270,18 279,40 282,65 L282,0 Z" fill="var(--maroon)"/>
      <path d="M0,45 C5,95 50,140 118,160 L0,160 Z" fill="var(--ink)"/>
      <path d="M0,62 C8,105 50,142 105,160 L0,160 Z" fill="var(--maroon)"/>
      <path d="M0,95 C12,125 40,148 75,160 L0,160 Z" fill="var(--ink)"/>
      <path d="M0,105 C14,130 38,150 62,160 L0,160 Z" fill="var(--maroon)"/>
    </svg>
    <div class="card-leaf" role="img" aria-label="Faint pale maple leaf decoration"></div>
    <div class="brand"><span class="brand-dot"></span>FERN &amp; COPPER</div>
    <div class="card-name">Maren Hollis</div>
    <div class="card-contact">
      <span class="site">www.fernandcopper.example</span>
      <span class="abn">ABN 62 307 514 928</span>
    </div>
  </section>

</main>
</body>
</html>
```